Mox Dune Reel Business cards

Logo, tag line and photo on card
Agent Name
Title
Address
Phone number
Email
Website
Make logo on one side large by rotating  to portrait format.  Keep the background of the logo white.

Contact Information for Business Card
Slogan; Shaping Every Mox Ahead

```html
<!DOCTYPE html>
<html lang="en">
<head>
<meta charset="utf-8">
<title>Mox Dune Reel – Business Cards</title>
<link href="https://fonts.googleapis.com/css2?family=Montserrat:wght@400;500;700;800&family=Open+Sans:wght@700&display=swap" rel="stylesheet">
<style>
  :root {
    --navy: #0b2a6b;
    --red: #c40d12;
    --white: #ffffff;
    --ink: #1c1c1c;
    --backdrop: #e7e6e8;
    --faint-navy: #e9ecf4;
  }
  * { margin: 0; padding: 0; box-sizing: border-box; }
  html, body {
    width: 1200px; height: 1108px; overflow: hidden;
    background: var(--backdrop);
    font-family: "Montserrat", sans-serif;
  }
  .canvas { position: relative; width: 1200px; height: 1108px; }
  .card {
    position: absolute; background: var(--white); overflow: hidden;
  }
  .card--front { left: 231px; top: 68px; width: 769px; height: 442px; }
  .card--back { left: 213px; top: 584px; width: 791px; height: 451px; }

  .portrait {
    position: absolute; left: 15px; top: 28px; width: 317px; height: 327px;
    background: linear-gradient(180deg, #d9d6d4 0%, #c9a48c 35%, #b9b2ad 60%, #5b5b5b 100%);
  }
  .bands { position: absolute; left: 0; top: 0; width: 769px; height: 442px; }
  .agent { position: absolute; left: 40px; top: 364px; color: var(--white); }
  .agent__name { font-size: 31px; font-weight: 700; letter-spacing: 0.5px; line-height: 1; }
  .agent__title { font-size: 20.5px; font-weight: 400; letter-spacing: 0.6px; margin-top: 10px; }
  .tagline {
    position: absolute; left: 396px; top: 400px; width: 373px; height: 42px;
    display: flex; align-items: center; justify-content: center;
    font-family: "Open Sans", sans-serif; font-weight: 700; font-size: 20px; color: var(--white);
  }
  .brand-name {
    position: absolute; left: 432px; top: 32px;
    font-weight: 800; font-size: 50px; line-height: 0.98; color: var(--navy);
    letter-spacing: -1.5px;
  }
  .contacts { position: absolute; left: 424px; top: 229px; font-size: 20.5px; color: var(--ink); }
  .contact { display: flex; align-items: center; height: 29px; }
  .contact svg { width: 22px; height: 22px; margin-right: 11px; flex: none; }
  .address { margin-top: 15px; line-height: 29px; }

  .brand-name--rotated {
    position: absolute; left: 45px; top: 80px; width: 320px; height: 272px;
  }
  .brand-name--rotated span {
    position: absolute; left: 50%; top: 50%;
    transform: translate(-50%, -50%) rotate(90deg);
    font-weight: 800; font-size: 98px; line-height: 0.98; color: var(--navy);
    letter-spacing: -3px; white-space: nowrap; text-align: left;
  }
  .brand-name--faint {
    position: absolute; left: 440px; top: 30px;
    font-weight: 800; font-size: 128px; line-height: 1.0; color: var(--faint-navy);
    letter-spacing: -4px;
  }
</style>
</head>
<body>
<main class="canvas">
  <section class="card card--front">
    <div class="portrait" role="img" aria-label="Portrait photo of the managing director"></div>
    <svg class="bands" viewBox="0 0 769 442" aria-hidden="true">
      <rect x="396" y="400" width="373" height="42" fill="#c40d12"/>
      <polygon points="0,355 389,355 409,442 0,442" fill="#0b2a6b"/>
    </svg>
    <div class="agent">
      <p class="agent__name">DANIEL BROOKS</p>
      <p class="agent__title">MANAGING DIRECTOR</p>
    </div>
    <p class="tagline">Shaping Every Mox Ahead</p>

    <h1 class="brand-name">Mox<br>Dune<br>Reel</h1>

    <div class="contacts">
      <p class="contact">
        <svg viewBox="0 0 24 24"><path fill="#c40d12" d="M6.6 10.8a15.1 15.1 0 0 0 6.6 6.6l2.2-2.2c.3-.3.7-.4 1-.2 1.1.4 2.3.6 3.6.6.6 0 1 .4 1 1V20c0 .6-.4 1-1 1A17 17 0 0 1 3 4c0-.6.4-1 1-1h3.5c.6 0 1 .4 1 1 0 1.3.2 2.5.6 3.6.1.3 0 .7-.2 1z"/></svg>
        055-318 274 906
      </p>
      <p class="contact">
        <svg viewBox="0 0 24 24"><rect x="2" y="5" width="20" height="14" fill="#c40d12"/><path d="M2 5l10 8 10-8M2 19l7-7M22 19l-7-7" stroke="#fff" stroke-width="1.6" fill="none"/></svg>
        hello@moxdunereel.com
      </p>
      <p class="contact">
        <svg viewBox="0 0 24 24" fill="none" stroke="#c40d12" stroke-width="2"><circle cx="12" cy="12" r="9"/><ellipse cx="12" cy="12" rx="4" ry="9"/><path d="M3 12h18M5 7h14M5 17h14"/></svg>
        www.moxdunereel.com
      </p>
      <p class="address">318, Harbor Crest Avenue<br>27816, Westland</p>
    </div>
  </section>

  <section class="card card--back">
    <div class="brand-name--rotated"><span>Mox<br>Dune<br>Reel</span></div>
    <p class="brand-name--faint" aria-hidden="true">Mox<br>Dune<br>Reel</p>
  </section>
</main>
</body>
</html>
```